Plumbing website that stands out

Seo optimized, mobile friendly, easily editable word press Plumbing website with google reviews widget. And widget of revolving photos of completed work. Contact page and services page, about page. Will provide, “About” content. And photos Need all other content written.
Services include:
Water heater replacement
Tankless water heater installation
Kitchen and bath remodel
Drain cleaning and clog removal
Leak repair
Faucet repair and replacement

I will be adding services and photos of recent completed projects as time goes on.

```html
<!DOCTYPE html>
<html lang="en">
<head>
<meta charset="utf-8">
<title>ClearFlow Plumbing</title>
<link href="https://fonts.googleapis.com/css2?family=Inter:wght@400;500;600;700&display=swap" rel="stylesheet">
<style>
:root{
  --blue:#2a5ea8;
  --blue-dark:#24589f;
  --teal:#67bfcf;
  --teal-light:#d7edf2;
  --ink:#1b1b1b;
  --muted:#444;
  --white:#fff;
  --dark-band:#1e4a55;
}
*{box-sizing:border-box;margin:0;padding:0}
html,body{width:1200px;height:3410px;overflow:hidden}
body{font-family:'Inter',sans-serif;color:var(--ink);background:var(--white);position:relative}
.abs{position:absolute}
a{color:inherit;text-decoration:none}

/* header */
.topbar{top:10px;right:68px;font-size:10px;color:#333;display:flex;gap:40px}
.topbar span{display:flex;align-items:center;gap:6px}
.logo{font-weight:600;color:var(--blue);text-align:center;letter-spacing:3px;line-height:1.2}
.header-logo{left:84px;top:48px;font-size:20px}
.header-logo small{display:block;font-size:9px;letter-spacing:5px}
.nav{left:326px;top:63px;display:flex;gap:48px;font-size:15px;font-weight:500}
.nav .active{color:var(--blue);border-bottom:2px solid var(--blue);padding-bottom:8px}
.help{left:803px;top:58px;font-size:10px}
.help strong{display:block;font-size:16px;color:var(--blue);font-weight:600;margin-top:3px}
.btn-schedule{left:955px;top:56px;width:181px;height:41px;border-radius:21px;background:var(--blue);color:#fff;font-size:15px;font-weight:500;display:flex;align-items:center;justify-content:center;gap:8px}
.header-line{top:116px;left:0;width:1200px;height:2px;background:#e8e8e8}

/* hero */
.hero-bg{top:118px;left:0;width:1200px;height:452px;background:linear-gradient(90deg,#fafafa 0%,#f1f3f3 50%,#e6e9ea 100%)}
.hero-person{top:140px;left:815px;width:290px;height:430px;background:linear-gradient(180deg,#e9ecee,#3a63c4 40%,#2c4fb0);border-radius:120px 120px 0 0}
.hero-title{left:80px;top:196px;font-size:29px;font-weight:600;line-height:36px}
.hero-title span{color:var(--blue)}
.hero-list{left:80px;top:296px;list-style:none;font-size:15px}
.hero-list li{display:flex;align-items:center;gap:14px;height:30px}
.btn-teal{background:var(--teal);color:#fff;border-radius:26px;display:flex;align-items:center;justify-content:center;gap:8px;font-size:13px;font-weight:500}
.hero-btn{left:80px;top:438px;width:193px;height:52px}

/* services */
.services-bg{top:556px;left:0;width:1200px;height:545px;background:var(--teal-light)}
.section-title{width:1200px;left:0;text-align:center;font-size:25px;font-weight:500}
.squiggle{display:block;margin:8px auto 0}
.card{background:#fff;box-shadow:0 2px 8px rgba(0,0,0,.08);width:284px;height:150px;display:flex;padding:18px 20px;gap:18px}
.card.featured{background:var(--teal);color:#fff}
.card .icon{width:70px;height:70px;border-radius:50%;background:var(--blue);flex:none;display:flex;align-items:center;justify-content:center}
.card h3{font-size:15px;font-weight:500;line-height:18px;margin-top:6px;min-height:36px}
.card .more{margin-top:12px;width:139px;height:42px;border:1.5px solid var(--blue);border-radius:21px;display:flex;align-items:center;justify-content:center;font-size:13px;font-weight:600;color:var(--blue)}
.card.featured .icon{background:var(--blue)}
.card.featured .more{border-color:#fff;color:#fff}

/* about */
.photo{background:linear-gradient(135deg,#c9d3de,#4c6f9e)}
.about-kicker{left:662px;top:1210px;font-size:15px;color:var(--blue)}
.about-title{left:662px;top:1240px;font-size:25px;font-weight:500}
.about-text{left:666px;top:1312px;width:410px;font-size:12.5px;line-height:22.5px;color:#222}
.about-btn{left:662px;top:1477px;width:130px;height:44px}

/* testimonials */
.testi-bg{top:1621px;left:0;width:1200px;height:588px;background:linear-gradient(135deg,#173a44,#2b5966 50%,#1a3e48)}
.testi-title{color:#fff}
.review{background:#fff;width:320px;height:223px;padding:26px 28px}
.review .who{display:flex;align-items:center;gap:8px;font-size:20px}
.review .avatar{width:44px;height:44px;border-radius:50%;background:#9aa3ad}
.review .stars{margin:14px 0 12px}
.review p{font-size:12.5px;line-height:15px}
.arrow{stroke:#fff;fill:none;stroke-width:2.5}
.dots{top:2044px;left:578px;display:flex;gap:6px}
.dots i{width:10px;height:10px;border-radius:50%;background:#fff}
.dots i:first-child{background:var(--teal)}
.rating{top:2095px;left:534px;width:175px;height:69px;background:#fff;border-top:3px solid #3cb55a;display:flex;align-items:center;gap:10px;padding:0 10px;font-size:11px}
.rating .mark{width:30px;height:30px;border-radius:50%;background:#d9d9d9;flex:none}
.rating b{color:#e0701e;font-size:15px;font-weight:500}
.rating small{color:#888;font-size:10px;display:block}

/* projects */
.project{top:2352px;height:288px;width:240px}
.btn-outline{border:1.5px solid var(--blue);border-radius:22px;color:var(--blue);font-size:13px;font-weight:600;display:flex;align-items:center;justify-content:center}

/* cta + footer */
.cta-text{left:204px;top:2826px;color:#fff;font-size:29px;font-weight:500}
.cta-btn{left:697px;top:2812px;width:259px;height:60px;background:#fff;border-radius:30px;font-size:15px;font-weight:600;color:var(--blue);display:flex;align-items:center;justify-content:center}
.info{top:2918px;width:298px;height:168px;background:#fff;text-align:center;padding-top:22px}
.info h4{color:var(--blue);font-size:15px;font-weight:600;margin:10px 0 12px}
.info p{font-size:12.5px}
.footer-logo{left:90px;top:3150px;color:#fff;font-size:28px;letter-spacing:5px}
.footer-logo small{display:block;font-size:10px;letter-spacing:8px}
.fcol{top:3150px;color:#fff}
.fcol h5{font-size:15px;font-weight:500;margin-bottom:18px}
.fcol li{list-style:none;font-size:12.5px;height:27px}
.social{display:flex;gap:14px}
.social i{width:20px;height:20px;border-radius:50%;background:#fff}
.bottom-bar{top:3364px;left:0;width:1200px;height:46px;background:#1f4f92;color:#fff;font-size:12.5px;text-align:center;line-height:46px}
</style>
</head>
<body>

<!-- Header -->
<div class="abs topbar">
  <span><svg width="12" height="14" viewBox="0 0 12 14"><path d="M6 1a4.5 4.5 0 0 0-4.5 4.5C1.5 9 6 13 6 13s4.5-4 4.5-7.5A4.5 4.5 0 0 0 6 1z" fill="none" stroke="#2a5ea8" stroke-width="1.2"/><circle cx="6" cy="5.5" r="1.5" fill="#2a5ea8"/></svg>Your location here</span>
  <span><svg width="14" height="10" viewBox="0 0 14 10"><rect x=".6" y=".6" width="12.8" height="8.8" fill="none" stroke="#2a5ea8" stroke-width="1.2"/><path d="M1 1l6 5 6-5" fill="none" stroke="#2a5ea8" stroke-width="1.2"/></svg>info@clearflowplumbing.com</span>
</div>
<div class="abs logo header-logo">CLEARFLOW<small>PLUMBING</small></div>
<nav class="abs nav">
  <a class="active">Home</a><a>About Us</a>
  <a>Services <svg width="12" height="8" viewBox="0 0 12 8"><path d="M1 1l5 5 5-5" fill="none" stroke="#222" stroke-width="1.5"/></svg></a>
  <a>Contact Us</a>
</nav>
<div class="abs help">Need Help Now? Call Us!<strong>&#9743; (555)014 2290</strong></div>
<a class="abs btn-schedule">Schedulle Online
  <svg width="17" height="17" viewBox="0 0 17 17"><rect x="1" y="3" width="15" height="13" rx="2" fill="none" stroke="#fff" stroke-width="1.5"/><path d="M5 1v4M12 1v4M5 10l2.5 2.5L12 8" fill="none" stroke="#fff" stroke-width="1.5"/></svg></a>
<div class="abs header-line"></div>

<!-- Hero -->
<div class="abs hero-bg" role="img" aria-label="Bright modern kitchen interior"></div>
<div class="abs hero-person" role="img" aria-label="Plumber in blue uniform and cap with arms crossed"></div>
<h1 class="abs hero-title">PROFESSIONAL PLUMBING<br><span>SERVICES AT AN AFFORDABLE PRICE</span></h1>
<ul class="abs hero-list">
  <li><svg width="14" height="14" viewBox="0 0 14 14"><circle cx="7" cy="7" r="6" fill="none" stroke="#222" stroke-width="1.3"/><path d="M4 7l2 2 4-4" fill="none" stroke="#222" stroke-width="1.3"/></svg>Local Plumber / Gas Fitter</li>
  <li><svg width="14" height="14" viewBox="0 0 14 14"><circle cx="7" cy="7" r="6" fill="none" stroke="#222" stroke-width="1.3"/><path d="M4 7l2 2 4-4" fill="none" stroke="#222" stroke-width="1.3"/></svg>Free Quotes</li>
  <li><svg width="14" height="14" viewBox="0 0 14 14"><circle cx="7" cy="7" r="6" fill="none" stroke="#222" stroke-width="1.3"/><path d="M4 7l2 2 4-4" fill="none" stroke="#222" stroke-width="1.3"/></svg>Qualified Plumbing and Gas Fitters</li>
  <li><svg width="14" height="14" viewBox="0 0 14 14"><circle cx="7" cy="7" r="6" fill="none" stroke="#222" stroke-width="1.3"/><path d="M4 7l2 2 4-4" fill="none" stroke="#222" stroke-width="1.3"/></svg>Maintenance Specialists</li>
</ul>
<a class="abs btn-teal hero-btn"><svg width="16" height="16" viewBox="0 0 16 16"><circle cx="8" cy="8" r="7" fill="none" stroke="#fff" stroke-width="1.2"/><path d="M5.5 4.5l1.5 2-1 1c.5 1 1.5 2 2.5 2.5l1-1 2 1.5-1 1.5C7.5 12 4 8.5 4 5.5z" fill="#fff"/></svg>GET FREE ESTIMATE</a>

<!-- Services -->
<div class="abs services-bg"></div>
<svg class="abs" style="top:520px;left:0" width="1200" height="70" viewBox="0 0 1200 70">
  <path d="M0 36C120 70 260 50 420 40S700 28 820 34 1060 8 1200 30V70H0z" fill="#d7edf2"/>
  <path d="M0 36C120 64 260 46 420 34S700 20 820 28 1060 4 1200 24V40C1060 20 900 40 820 42S580 40 420 50 120 78 0 50z" fill="#67bfcf"/>
</svg>
<h2 class="abs section-title" style="top:647px">OUR SERVICES
  <svg class="squiggle" width="70" height="10" viewBox="0 0 70 10"><path d="M2 6c8-6 14 2 22 0s14-6 22 0 14 2 22-2" fill="none" stroke="#2a5ea8" stroke-width="2.5"/></svg></h2>

<div class="abs card" style="left:143px;top:723px">
  <div class="icon"><svg width="30" height="40" viewBox="0 0 30 40"><rect x="4" y="2" width="22" height="32" rx="3" fill="none" stroke="#fff" stroke-width="2.5"/><circle cx="15" cy="14" r="5" fill="none" stroke="#fff" stroke-width="2"/><path d="M9 38v-4M21 38v-4" stroke="#fff" stroke-width="2.5"/></svg></div>
  <div><h3>WATER HEATER<br>REPLACEMENT</h3><a class="more">LEARN MORE</a></div>
</div>
<div class="abs card featured" style="left:458px;top:723px">
  <div class="icon"><svg width="34" height="38" viewBox="0 0 34 38"><rect x="3" y="4" width="28" height="30" rx="4" fill="#fff"/><path d="M3 12h28M3 19h28M3 26h28" stroke="#2a5ea8" stroke-width="2"/></svg></div>
  <div><h3>TANKLESS<br>WATER HEATER<br>INSTALLATION</h3><a class="more">LEARN MORE</a></div>
</div>
<div class="abs card" style="left:772px;top:723px">
  <div class="icon"><svg width="38" height="30" viewBox="0 0 38 30"><rect x="2" y="4" width="34" height="22" fill="none" stroke="#fff" stroke-width="2.5"/><rect x="7" y="10" width="10" height="10" fill="none" stroke="#fff" stroke-width="2"/><rect x="21" y="10" width="10" height="10" fill="none" stroke="#fff" stroke-width="2"/></svg></div>
  <div><h3>KITCHEN AND<br>BATH REMODEL</h3><a class="more">LEARN MORE</a></div>
</div>
<div class="abs card" style="left:143px;top:890px">
  <div class="icon"><svg width="34" height="34" viewBox="0 0 34 34"><path d="M26 4l4 4-12 12-4-4z" fill="#fff"/><path d="M14 16l4 4-8 10-6-6z" fill="none" stroke="#fff" stroke-width="2.5"/></svg></div>
  <div><h3>DRAIN CLEANING<br>AND CLOG REMOVAL</h3><a class="more">LEARN MORE</a></div>
</div>
<div class="abs card" style="left:458px;top:890px">
  <div class="icon"><svg width="40" height="36" viewBox="0 0 40 36"><path d="M4 4v14M36 4v14M4 11h32" stroke="#fff" stroke-width="3"/><rect x="12" y="5" width="16" height="12" fill="#fff"/><path d="M20 22c-3 4-3 6 0 8 3-2 3-4 0-8z" fill="#fff"/></svg></div>
  <div><h3>LEAK REPAIR</h3><a class="more">LEARN MORE</a></div>
</div>
<div class="abs card" style="left:772px;top:890px">
  <div class="icon"><svg width="30" height="36" viewBox="0 0 30 36"><path d="M8 34V14a8 8 0 0 1 16 0v4" fill="none" stroke="#fff" stroke-width="3"/><path d="M20 18h8" stroke="#fff" stroke-width="3"/><path d="M4 26h8" stroke="#fff" stroke-width="3"/></svg></div>
  <div><h3>FAUCET REPAIR AND<br>REPLACEMENT</h3><a class="more">LEARN MORE</a></div>
</div>
<svg class="abs" style="top:1070px;left:0" width="1200" height="50" viewBox="0 0 1200 50"><path d="M0 26C300 6 800 6 1200 24V50H0z" fill="#fff"/></svg>

<!-- About -->
<div class="abs photo" style="left:73px;top:1163px;width:424px;height:297px" role="img" aria-label="Smiling plumber in cap working under a kitchen sink"></div>
<div class="abs photo" style="left:278px;top:1327px;width:315px;height:223px;background:linear-gradient(135deg,#d8dde2,#5a6e8c 60%,#c0392b)" role="img" aria-label="Plumber holding a tool bag with wrench and hoses"></div>
<div class="abs about-kicker">ABOUT COMPANY</div>
<h2 class="abs about-title">CLEARFLOW PLUMBING
  <svg style="display:block;margin-top:8px" width="70" height="10" viewBox="0 0 70 10"><path d="M2 6c8-6 14 2 22 0s14-6 22 0 14 2 22-2" fill="none" stroke="#2a5ea8" stroke-width="2.5"/></svg></h2>
<p class="abs about-text">Lorem ipsum dolor sit amet consectetur. In nunc non scelerisque rhoncus. Ac fusce ipsum pharetra eu. Enim et augue urna turpis. Turpis libero at facilisi vulputate lobortis lectus dignissim. Faucibus dictumst in diam donec. Malesuada dolor ullamcorper lorem potenti sem leo. Elementum eu leo praesent sed. Non tincidunt purus massa eget scelerisque. Porta nullam ultrices eget metus nunc mauris leo sed.</p>
<a class="abs btn-teal about-btn">LEARN MORE</a>

<!-- Testimonials -->
<div class="abs testi-bg" role="img" aria-label="Dark teal toned photo of hands fixing pipes under a sink"></div>
<h2 class="abs section-title testi-title" style="top:1699px">CLIENTS TESTIMONIALS
  <svg class="squiggle" width="70" height="10" viewBox="0 0 70 10"><path d="M2 6c8-6 14 2 22 0s14-6 22 0 14 2 22-2" fill="none" stroke="#fff" stroke-width="2.5"/></svg></h2>
<svg class="abs" style="left:60px;top:1866px" width="22" height="40" viewBox="0 0 22 40"><path class="arrow" d="M20 2L3 20l17 18"/></svg>
<svg class="abs" style="left:1120px;top:1856px" width="22" height="40" viewBox="0 0 22 40"><path class="arrow" d="M2 2l17 18L2 38"/></svg>

<div class="abs review" style="left:103px;top:1776px">
  <div class="who"><span class="avatar"></span>Dana Whitfield</div>
  <svg class="stars" width="150" height="26" viewBox="0 0 150 26"><g fill="#f5b50a"><polygon id="st" points="13,1 16.5,9.5 25.5,9.5 18.2,15 21,24 13,18.5 5,24 7.8,15 0.5,9.5 9.5,9.5"/><use href="#st" x="30"/><use href="#st" x="60"/><use href="#st" x="90"/><use href="#st" x="120"/></g></svg>
  <p>The technician was polite and took care of a simple water heater problem and Took the time to explain things to me. I am very pleased</p>
</div>
<div class="abs review" style="left:444px;top:1778px">
  <div class="who"><span class="avatar"></span>Marcus Hale</div>
  <svg class="stars" width="150" height="26" viewBox="0 0 150 26"><g fill="#f5b50a"><use href="#st"/><use href="#st" x="30"/><use href="#st" x="60"/><use href="#st" x="90"/><use href="#st" x="120"/></g></svg>
  <p>The technician was polite and took care of a simple water heater problem and Took the time to explain things to me. I am very pleased</p>
</div>
<div class="abs review" style="left:776px;top:1778px">
  <div class="who"><span class="avatar"></span>Dana Whitfield</div>
  <svg class="stars" width="150" height="26" viewBox="0 0 150 26"><g fill="#f5b50a"><use href="#st"/><use href="#st" x="30"/><use href="#st" x="60"/><use href="#st" x="90"/><use href="#st" x="120"/></g></svg>
  <p>The technician was polite and took care of a simple water heater problem and Took the time to explain things to me. I am very pleased</p>
</div>
<div class="abs dots"><i></i><i></i><i></i></div>
<div class="abs rating"><span class="mark"></span>
  <div>Review Rating<br><b>5.0</b> <span style="color:#e0701e;font-size:14px">★★★★★</span><small>See all our reviews</small></div>
</div>

<!-- Projects -->
<h2 class="abs section-title" style="top:2276px">OUR RECENT PROJECTS
  <svg class="squiggle" width="70" height="10" viewBox="0 0 70 10"><path d="M2 6c8-6 14 2 22 0s14-6 22 0 14 2 22-2" fill="none" stroke="#2a5ea8" stroke-width="2.5"/></svg></h2>
<svg class="abs" style="left:56px;top:2494px" width="22" height="40" viewBox="0 0 22 40"><path d="M20 2L3 20l17 18" fill="none" stroke="#666" stroke-width="2.5"/></svg>
<svg class="abs" style="left:1122px;top:2494px" width="22" height="40" viewBox="0 0 22 40"><path d="M2 2l17 18L2 38" fill="none" stroke="#666" stroke-width="2.5"/></svg>
<div class="abs project photo" style="left:122px;background:linear-gradient(135deg,#c8b9a3,#4a73b8)" role="img" aria-label="Plumber installing a kitchen faucet"></div>
<div class="abs project photo" style="left:368px;background:linear-gradient(135deg,#b9bcc0,#3a3d42)" role="img" aria-label="Hand adjusting a running kitchen tap"></div>
<div class="abs project photo" style="left:616px;background:linear-gradient(135deg,#e4e7ea,#2b2b2b)" role="img" aria-label="Gloved hands tightening a pipe with a wrench"></div>
<div class="abs project photo" style="left:862px;background:linear-gradient(135deg,#f0f0f0,#333 60%,#999)" role="img" aria-label="Close-up of a chrome faucet in black and white"></div>
<a class="abs btn-outline" style="left:530px;top:2678px;width:139px;height:43px">MORE PROJECTS</a>

<!-- CTA -->
<svg class="abs" style="top:2728px;left:0" width="1200" height="282" viewBox="0 0 1200 282">
  <path d="M0 18C300 -2 700 26 1000 12S1180 8 1200 10V282H0z" fill="#67bfcf"/>
</svg>
<div class="abs" style="top:3007px;left:0;width:1200px;height:357px;background:var(--blue-dark)"></div>
<div class="abs cta-text">HAVE A PLUMBING PROBLEM?</div>
<a class="abs cta-btn">GET FREE ESTIMATE NOW</a>

<div class="abs info" style="left:117px">
  <svg width="34" height="42" viewBox="0 0 34 42"><path d="M17 2a11 11 0 0 0-11 11c0 8 11 19 11 19s11-11 11-19A11 11 0 0 0 17 2z" fill="#2a5ea8"/><circle cx="17" cy="13" r="4" fill="#fff"/><path d="M2 40l6-10h18l6 10z" fill="none" stroke="#67bfcf" stroke-width="2"/></svg>
  <h4>ADDRESS:</h4><p>Your Location here</p>
</div>
<div class="abs info" style="left:432px">
  <svg width="40" height="42" viewBox="0 0 40 42"><path d="M8 8l7 8-3 4c2 4 6 8 10 10l4-3 8 7-4 5C16 39 3 26 4 12z" fill="#2a5ea8"/><path d="M24 6a12 12 0 0 1 10 10M24 12a6 6 0 0 1 5 5" fill="none" stroke="#67bfcf" stroke-width="2"/></svg>
  <h4>PHONE NUMBERS:</h4><p style="font-size:20px">(555)014 2290</p>
</div>
<div class="abs info" style="left:746px">
  <svg width="44" height="44" viewBox="0 0 44 44"><circle cx="22" cy="22" r="19" fill="none" stroke="#2a5ea8" stroke-width="3"/><circle cx="22" cy="22" r="13" fill="none" stroke="#67bfcf" stroke-width="2"/><path d="M22 13v9l6 4" fill="none" stroke="#2a5ea8" stroke-width="2.5"/></svg>
  <h4>WORKING TIME:</h4><p>24 Hour Service - 7 Days a<br>Week365 Days</p>
</div>

<!-- Footer -->
<div class="abs logo footer-logo">CLEARFLOW<small>PLUMBING</small></div>
<div class="abs fcol" style="left:404px">
  <h5>QUICKLINKS</h5>
  <ul><li>Home</li><li>About Us</li><li>Our Services</li><li>Contact Us</li></ul>
</div>
<div class="abs fcol" style="left:600px">
  <h5>SERVICES</h5>
  <ul><li>Water heater replacement</li><li>Tankless water heater installation</li><li>Kitchen and bath remodel</li><li>Drain cleaning and clog removal</li><li>Leak repairFaucet repair and replacement</li></ul>
</div>
<div class="abs fcol" style="left:889px;top:3146px">
  <h5>CONNECTED WITH US</h5>
  <div class="social"><i></i><i></i><i></i><i></i><i></i></div>
</div>
<div class="abs bottom-bar">©2022 CLEARFLOW PLUMBING. All rights reserved.</div>

</body>
</html>
```